Spanish winery needs a label design for a red, white and rosé wine.

We need a front and back label for our representee Garrido Velasquez SL, a wine producer in the Spanish region of Extremadura.

Trademark: Sereneto. Sereneto means balanced in English. The message is that the wine show the equilibrium of the blends specially produced for this project, it is balanced in the mounth and nose and it,s a good balance between quality and price.

Target: Wine targets entry level market retail sector in Europe so it cannot be too fancy.

Style: Spanish wines are better seen with a classic touch in the design although a bit of modernity is required.

Number of labels: 3 front and 3 back labels required although you can use the same design and just change the colors. Bottle is a bordeaux style 30 mm high with an screw cup closure, green for the red and transparent for the white and rosé.

Labels size: front max 90 (wide)x130 (high)mm. Back max 85 (w)x85(h)mm.

Information to include in the front label: Trademark, type of wine (red, white or rosé), two short lines of text with tasting notes (see texts on doc file), capacity 75cl, ABV:11º vol. Bottled by Garrido Velásquez SL C/Almadena 27. 06480 Villar del Caminal (Badajoz). Spain.

Information to be included in the back label:trademark, type of wine, tasting notes (see texts on doc file), Capacity 75cl, Filling control mark: E, Barcode, Allergy advise, Contains sulfites advise, Pregnant women advise.

Paper: Shiny or matt paper with possibility of foil printing. No embossed effects.

Please see attached Val de Piedra label as a reference of the necessary information to be contained by labels.
Updates

Reason: We would like to give a bit more of time to those that have accepted and have not yet submitted a design.

Target Market(s)

Entry level european consumers

Industry/Entity Type

Retail

Requirements
Nice to have
• Maybe a clasical scale, old coins (balanced in cost).... Balance is the route to follow.

```html
<!DOCTYPE html>
<html lang="en">
<head>
<meta charset="utf-8">
<title>Sereneto – Front and Back Labels</title>
<link rel="stylesheet" href="https://fonts.googleapis.com/css2?family=Didact+Gothic&display=swap">
<style>
  :root {
    --cream: #f1ecda;
    --paper: #ffffff;
    --lime: #b6bd2c;
    --lime-ink: #3d3f24;
    --red: #e0352b;
    --red-ink: #3a2a27;
    --maroon: #6a1b1f;
    --maroon-ink: #5a1a1c;
    --light: #fdfbf3;
  }
  * { margin: 0; padding: 0; box-sizing: border-box; }
  html, body { width: 757px; height: 1200px; overflow: hidden; }
  body {
    background: var(--paper);
    font-family: "Didact Gothic", "Helvetica Neue", Arial, sans-serif;
    position: relative;
  }
  h2, h3, strong { font-weight: normal; }
  .label-row { position: absolute; left: 0; width: 757px; height: 370px; }
  .row-white { top: 22px; --band: var(--lime); --ink: var(--lime-ink); }
  .row-rose { top: 412px; --band: var(--red); --ink: var(--red-ink); }
  .row-tinto { top: 802px; --band: var(--maroon); --ink: var(--maroon-ink); }

  .front-label { position: absolute; left: 42px; top: 0; width: 260px; height: 370px; }
  .back-label { position: absolute; left: 360px; top: 54px; width: 360px; height: 263px; }
  .label-shape { position: absolute; inset: 0; width: 100%; height: 100%; display: block; }
  .label-shape .band { fill: var(--band); }
  .label-shape .field { fill: var(--cream); }

  .tagline { position: absolute; left: 0; right: 0; text-align: center; font-size: 10px; color: var(--ink); }
  .brand { position: absolute; left: 0; right: 0; text-align: center; color: var(--ink); letter-spacing: 1.5px; }
  .front-label .tagline { top: 40px; }
  .front-label .brand { top: 52px; font-size: 25px; }

  .balance-art {
    position: absolute; left: 50px; top: 96px; width: 160px; height: 72px;
    border-radius: 50%;
    background: radial-gradient(ellipse at center, #8f8b82 0%, #c7c2b4 55%, rgba(241,236,218,0) 75%);
  }
  .wine-type { position: absolute; left: 0; right: 0; top: 178px; text-align: center; font-size: 21px; color: var(--ink); }

  .tasting-note {
    position: absolute; left: 30px; right: 30px; top: 246px;
    text-align: center; font-size: 9px; line-height: 1.35; color: var(--light);
  }
  .volume, .abv { position: absolute; top: 296px; font-size: 13px; color: var(--light); }
  .volume { left: 14px; }
  .abv { right: 14px; }
  .bottler {
    position: absolute; left: 10px; right: 10px; top: 322px;
    text-align: center; font-size: 7.5px; line-height: 1.4; color: var(--light);
  }

  .back-label .tagline { top: 34px; font-size: 9px; }
  .back-label .brand { top: 45px; font-size: 21px; }
  .back-notes {
    position: absolute; left: 22px; top: 100px; width: 150px;
    text-align: center; font-size: 8px; line-height: 1.4; color: var(--light);
  }
  .back-warning {
    position: absolute; left: 194px; top: 100px; width: 146px;
    font-size: 7px; line-height: 1.45; text-transform: uppercase; color: var(--light);
  }
  .back-footer {
    position: absolute; right: 20px; top: 222px;
    color: var(--light); font-size: 8px; letter-spacing: .4px;
  }
  .back-footer .cap { font-size: 14px; margin-right: 4px; }
</style>
</head>
<body>

<section class="label-row row-white">
  <article class="front-label">
    <svg class="label-shape" viewBox="0 0 260 370" preserveAspectRatio="none" aria-hidden="true">
      <rect class="band" width="260" height="370"/>
      <path class="field" d="M0 34 L10 30 L18 33 L30 27 L44 30 L58 25 L70 29 L86 23 L100 27 L116 22 L130 26 L146 20 L160 24 L176 19 L190 23 L206 18 L220 22 L236 17 L248 21 L260 16 L260 222 C215 246 160 206 110 222 C70 234 30 234 0 224 Z"/>
    </svg>
    <p class="tagline">Poised in every glass</p>
    <h2 class="brand">SERENETO</h2>
    <div class="balance-art" role="img" aria-label="Engraved illustration of three stones balanced on a plank"></div>
    <h3 class="wine-type">White</h3>
    <p class="tasting-note">A crisp, refreshing Spanish white wine bursting with crisp apple and tropical fruits flavours.</p>
    <span class="volume">75cl</span>
    <span class="abv">11º vol.</span>
    <p class="bottler">Bottled by<br>Garrido Velásquez SL. C/Almadena 27.<br>06480 Villar del Caminal (Badajoz). Spain</p>
  </article>
  <article class="back-label">
    <svg class="label-shape" viewBox="0 0 360 263" preserveAspectRatio="none" aria-hidden="true">
      <rect class="band" width="360" height="263"/>
      <path class="field" d="M0 26 L14 22 L26 25 L42 19 L58 23 L74 17 L90 21 L108 15 L124 19 L142 14 L160 18 L178 12 L196 16 L214 11 L232 15 L250 10 L268 14 L286 9 L304 13 L322 8 L340 12 L360 7 L360 72 C300 90 240 64 180 76 C120 88 60 86 0 76 Z"/>
    </svg>
    <p class="tagline">Poised in every glass</p>
    <h2 class="brand">SERENETO</h2>
    <p class="back-notes">Sereneto is a delicious fresh white wine, full of ripe apple and juicy pineapple flavours. It is a great partner to pasta or chicken salads. Serve well chilled.</p>
    <p class="back-warning"><strong>Allergens warning:</strong> Contains sulfites. Drinking alcohol during pregnancy, even in small amounts, can harm the baby. Please drink responsibly and keep away from children.</p>
    <p class="back-footer"><span class="cap">75cl</span> CONTAINS SULFITES</p>
  </article>
</section>

<section class="label-row row-rose">
  <article class="front-label">
    <svg class="label-shape" viewBox="0 0 260 370" preserveAspectRatio="none" aria-hidden="true">
      <rect class="band" width="260" height="370"/>
      <path class="field" d="M0 34 L10 30 L18 33 L30 27 L44 30 L58 25 L70 29 L86 23 L100 27 L116 22 L130 26 L146 20 L160 24 L176 19 L190 23 L206 18 L220 22 L236 17 L248 21 L260 16 L260 222 C215 246 160 206 110 222 C70 234 30 234 0 224 Z"/>
    </svg>
    <p class="tagline">Poised in every glass</p>
    <h2 class="brand">SERENETO</h2>
    <div class="balance-art" role="img" aria-label="Engraved illustration of three stones balanced on a plank"></div>
    <h3 class="wine-type">Rosé</h3>
    <p class="tasting-note">A refreshing Spanish Rosado bursting with ripe strawberry and cherry flavours.</p>
    <span class="volume">75cl</span>
    <span class="abv">11º vol.</span>
    <p class="bottler">Bottled by<br>Garrido Velásquez SL. C/Almadena 27.<br>06480 Villar del Caminal (Badajoz). Spain</p>
  </article>
  <article class="back-label">
    <svg class="label-shape" viewBox="0 0 360 263" preserveAspectRatio="none" aria-hidden="true">
      <rect class="band" width="360" height="263"/>
      <path class="field" d="M0 26 L14 22 L26 25 L42 19 L58 23 L74 17 L90 21 L108 15 L124 19 L142 14 L160 18 L178 12 L196 16 L214 11 L232 15 L250 10 L268 14 L286 9 L304 13 L322 8 L340 12 L360 7 L360 72 C300 90 240 64 180 76 C120 88 60 86 0 76 Z"/>
    </svg>
    <p class="tagline">Poised in every glass</p>
    <h2 class="brand">SERENETO</h2>
    <p class="back-notes">This fresh and elegant rosé wine features aromas of ripe strawberry and cherry. A great wine to enjoy on its own or with light summer dishes. Serve chilled.</p>
    <p class="back-warning"><strong>Allergens warning:</strong> Contains sulfites. Drinking alcohol during pregnancy, even in small amounts, can harm the baby. Please drink responsibly and keep away from children.</p>
    <p class="back-footer"><span class="cap">75cl</span> CONTAINS SULFITES</p>
  </article>
</section>

<section class="label-row row-tinto">
  <article class="front-label">
    <svg class="label-shape" viewBox="0 0 260 370" preserveAspectRatio="none" aria-hidden="true">
      <rect class="band" width="260" height="370"/>
      <path class="field" d="M0 34 L10 30 L18 33 L30 27 L44 30 L58 25 L70 29 L86 23 L100 27 L116 22 L130 26 L146 20 L160 24 L176 19 L190 23 L206 18 L220 22 L236 17 L248 21 L260 16 L260 222 C215 246 160 206 110 222 C70 234 30 234 0 224 Z"/>
    </svg>
    <p class="tagline">Poised in every glass</p>
    <h2 class="brand">SERENETO</h2>
    <div class="balance-art" role="img" aria-label="Engraved illustration of three stones balanced on a plank"></div>
    <h3 class="wine-type">Tinto</h3>
    <p class="tasting-note">Seductively soft and smooth red wine displaying delicious fruit flavours.</p>
    <span class="volume">75cl</span>
    <span class="abv">11º vol.</span>
    <p class="bottler">Bottled by<br>Garrido Velásquez SL. C/Almadena 27.<br>06480 Villar del Caminal (Badajoz). Spain</p>
  </article>
  <article class="back-label">
    <svg class="label-shape" viewBox="0 0 360 263" preserveAspectRatio="none" aria-hidden="true">
      <rect class="band" width="360" height="263"/>
      <path class="field" d="M0 26 L14 22 L26 25 L42 19 L58 23 L74 17 L90 21 L108 15 L124 19 L142 14 L160 18 L178 12 L196 16 L214 11 L232 15 L250 10 L268 14 L286 9 L304 13 L322 8 L340 12 L360 7 L360 72 C300 90 240 64 180 76 C120 88 60 86 0 76 Z"/>
    </svg>
    <p class="tagline">Poised in every glass</p>
    <h2 class="brand">SERENETO</h2>
    <p class="back-notes">This is a soft, easy drinking dry red wine, full of delicious ripe fruit flavours. Enjoy it with tapas, grilled meat or cheese. Serve at room temperature.</p>
    <p class="back-warning"><strong>Allergens warning:</strong> Contains sulfites. Drinking alcohol during pregnancy, even in small amounts, can harm the baby. Please drink responsibly and keep away from children.</p>
    <p class="back-footer"><span class="cap">75cl</span> CONTAINS SULFITES</p>
  </article>
</section>

</body>
</html>
```